Yard Sign Design for luxury design & build company

Looking to have 18" x 24" company yard signs designed.
An update to the business logo might be helpful.
Photos are not necessary but use if you can make inspiring.

Industry: Construction

Looking for a large headline of "Basement Finishing"
Website: www.tamberlyhomes.com
Phone Number (612) 555-0174
FB link: facebook.com/tamberlyhomesmn
Instagram: www.instagram.com/tamberlyhomesmn

Industry/Entity Type

Construction

Colors

Designer to choose colors to be used in the design.

Requirements
Must have
• Impactful high end characteristics
Nice to have
• Depth and detail graphis

```html
<!DOCTYPE html>
<html lang="en">
<head>
<meta charset="utf-8">
<title>Basement Finishing Yard Sign – Tamberly Homes</title>
<link rel="stylesheet" href="https://fonts.googleapis.com/css2?family=Bebas+Neue&family=Montserrat:wght@800&display=swap">
<style>
  :root {
    --backdrop: #c4c4c4;
    --ink: #111111;
    --paper: #ffffff;
    --brand-red: #d9261c;
    --dark-top: #0d0d0d;
    --dark-bottom: #2c2c2c;
    --badge: #ececec;
  }
  * { margin: 0; padding: 0; box-sizing: border-box; }
  html, body {
    width: 1200px; height: 2272px; overflow: hidden;
    background: var(--backdrop);
  }
  .yard-sign {
    position: absolute; left: 80px; top: 442px;
    width: 1040px; height: 1387px;
    background: var(--paper);
    box-shadow: 0 6px 18px rgba(0,0,0,.25);
    overflow: hidden;
  }
  .hero-photo {
    position: absolute; left: 0; top: 0; width: 100%; height: 696px;
    background:
      radial-gradient(ellipse at 60% 55%, rgba(90,90,90,.45), transparent 65%),
      linear-gradient(180deg, var(--dark-top), var(--dark-bottom));
  }
  .headline {
    position: absolute; left: 0; width: 100%;
    font-family: "Bebas Neue", "Oswald", sans-serif;
    font-weight: 400;
    text-align: center; line-height: 1; white-space: nowrap;
  }
  .headline--white { top: 96px; font-size: 268px; color: var(--paper); letter-spacing: 2px; }
  .headline--red { top: 338px; font-size: 298px; color: var(--brand-red); letter-spacing: -1px; }
  .phone-bar {
    position: absolute; left: 70px; top: 638px; width: 896px; height: 156px;
    background: var(--brand-red); border-radius: 14px;
    display: flex; align-items: center;
    overflow: hidden;
  }
  .phone-icon {
    flex: 0 0 88px; width: 88px; height: 88px; margin-left: 25px; border-radius: 50%;
    background: var(--ink); display: flex; align-items: center; justify-content: center;
  }
  .phone-number {
    font-family: "Bebas Neue", "Oswald", sans-serif;
    color: var(--paper); font-size: 146px; line-height: 1;
    margin-left: 26px; padding-top: 12px; letter-spacing: 0;
    white-space: nowrap;
  }
  .website {
    position: absolute; left: 0; top: 820px; width: 100%; text-align: center;
    font-family: "Montserrat", sans-serif; font-weight: 800;
    font-size: 61px; line-height: 1; color: var(--ink); letter-spacing: -0.5px;
    white-space: nowrap;
  }
  .brand-mark {
    position: absolute; left: 192px; top: 916px;
    width: 213px; height: 213px; border-radius: 50%;
    border: 8px solid var(--brand-red);
  }
  .brand-name {
    position: absolute; left: 434px; top: 1012px;
    font-family: "Bebas Neue", "Oswald", sans-serif;
    font-size: 72px; line-height: 1; color: var(--ink); letter-spacing: 1px;
    white-space: nowrap;
  }
  .review-badge {
    position: absolute; left: 70px; top: 1184px; width: 357px; height: 126px;
    background: var(--badge); border-radius: 14px;
  }
  .social-dot {
    position: absolute; left: 474px; top: 1148px;
    width: 74px; height: 74px; border-radius: 50%; background: var(--brand-red);
  }
  .social-handle {
    position: absolute; left: 474px; top: 1240px;
    font-family: "Bebas Neue", "Oswald", sans-serif;
    font-size: 72px; line-height: 1; color: var(--ink); letter-spacing: 0;
    white-space: nowrap;
  }
</style>
</head>
<body>
  <main class="yard-sign">
    <div class="hero-photo" role="img" aria-label="Darkened photo of a finished basement living room"></div>
    <h1>
      <span class="headline headline--white">BASEMENT</span>
      <span class="headline headline--red">FINISHING</span>
    </h1>
    <div class="phone-bar">
      <div class="phone-icon">
        <svg width="50" height="50" viewBox="0 0 24 24" aria-hidden="true">
          <path fill="#ffffff" d="M6.6 10.8a15.1 15.1 0 0 0 6.6 6.6l2.2-2.2a1 1 0 0 1 1-.25 11.4 11.4 0 0 0 3.6.57 1 1 0 0 1 1 1V20a1 1 0 0 1-1 1A17 17 0 0 1 3 4a1 1 0 0 1 1-1h3.5a1 1 0 0 1 1 1c0 1.25.2 2.45.57 3.6a1 1 0 0 1-.25 1z"/>
        </svg>
      </div>
      <span class="phone-number">(612) 555-0174</span>
    </div>
    <p class="website">www.tamberlyhomes.com</p>
    <div class="brand-mark"></div>
    <span class="brand-name">TAMBERLY HOMES</span>
    <div class="review-badge" role="img" aria-label="Five-star customer review badge"></div>
    <div class="social-dot"></div>
    <span class="social-handle">@TAMBERLYHOMESMN</span>
  </main>
</body>
</html>
```